Gourmet cookie company needs a label designed

We need a label designed for a new cookie company. We make mini cookies. The labels will be placed on either white tins or clear containers. We would like some bright and eye catching label although not child like. Our target customer is adults not kids.
Any color/colors acceptable. The initial label will be a square 4" label but the design should also be able to be formatted to fit on a round label as well in the future.

Text on label: Rosalind's Wafer Crumb Company; Chocolate Chip; All Natural; New Wt. 8.0oz

```html
<!DOCTYPE html>
<html lang="en">
<head>
<meta charset="utf-8">
<title>Rosalind's Wafer Crumb Company – Chocolate Chip Cookies Label</title>
<link rel="stylesheet" href="https://fonts.googleapis.com/css2?family=Josefin+Sans:wght@300;400&family=Marcellus&family=Tinos&display=swap">
<style>
  :root {
    --backdrop: #e4e4e4;
    --label-white: #ffffff;
    --frame-gold: #d8c69a;
    --cocoa: #3a1412;
    --ink: #3c3c3c;
    --rule-grey: #8a8a8a;
    --band-text: #ffffff;
  }
  html, body {
    margin: 0;
    padding: 0;
    width: 1200px;
    height: 900px;
    overflow: hidden;
    background: var(--backdrop);
  }
  .canvas {
    position: relative;
    width: 1200px;
    height: 900px;
  }
  .label {
    position: absolute;
    left: 450px;
    top: 296px;
    width: 280px;
    height: 281px;
    background: var(--label-white);
    border: 3px solid var(--frame-gold);
    box-sizing: content-box;
  }
  .brand {
    position: absolute;
    left: 0;
    right: 0;
    top: 26px;
    display: flex;
    flex-direction: column;
    align-items: center;
    gap: 8px;
  }
  .brand-dot {
    width: 26px;
    height: 26px;
    border-radius: 50%;
    background: var(--cocoa);
  }
  .brand-name {
    margin: 0;
    width: 180px;
    text-align: center;
    font-family: "Marcellus", serif;
    font-size: 14px;
    line-height: 1.25;
    color: var(--cocoa);
    letter-spacing: 0.5px;
  }
  .product {
    position: absolute;
    left: 68px;
    width: 154px;
    top: 141px;
    height: 54px;
    border-top: 1px solid var(--rule-grey);
    border-bottom: 1px solid var(--rule-grey);
    text-align: center;
    font-family: "Josefin Sans", sans-serif;
    font-weight: 300;
    color: var(--ink);
  }
  .product-flavour {
    display: block;
    margin-top: 8px;
    font-size: 14px;
    letter-spacing: 0.6px;
    line-height: 16px;
  }
  .product-type {
    display: block;
    margin-top: 3px;
    font-size: 15px;
    letter-spacing: 1.6px;
    line-height: 18px;
  }
  .net-weight {
    position: absolute;
    left: 0;
    right: 0;
    top: 232px;
    margin: 0;
    text-align: center;
    font-family: "Tinos", serif;
    font-size: 9px;
    line-height: 11px;
    color: var(--ink);
  }
  .claim-band {
    position: absolute;
    left: 0;
    right: 0;
    bottom: 0;
    height: 31px;
    background: var(--cocoa);
    color: var(--band-text);
    font-family: "Marcellus", serif;
    font-size: 14px;
    letter-spacing: 0.4px;
    line-height: 32px;
    text-align: center;
  }
</style>
</head>
<body>
  <div class="canvas">
    <section class="label">
      <header class="brand">
        <span class="brand-dot"></span>
        <p class="brand-name">Rosalind's Wafer Crumb Company</p>
      </header>
      <div class="product">
        <span class="product-flavour">CHOCOLATE CHIP</span>
        <span class="product-type">COOKIES</span>
      </div>
      <p class="net-weight">Net WT. 8.0 oz</p>
      <div class="claim-band">ALL NATURAL</div>
    </section>
  </div>
</body>
</html>
```